Escape Room Flyer Design - Start up. A5

Flyer is for letterbox drops to get interest and let people know that our business exists and to a lesser extent what an escape room is. We have 1 room (the miller's shadows) and a second room coming soon (Varuna's Vault). I have attached our logo and 2 flyers that I have seen in the past that I really like the design of.
Whether you are having a night out with friends or family, celebrating a special event, planning a team-building activity, or simply wanting a diversion from the doldrums of your workweek, The Lock Box will provide you an unforgettable live-action gaming experience.

Target Market(s)

18-25

Industry/Entity Type

Entertainment

Requirements
Must have
• Logo. Phone number 0417 265 839. Website. www.thelockboxhartwell.com
Bookings essential.
Nice to have
• Mystery, a little bit on the darker side than bright colourful and blocky.
"Many Will Enter…Few Will Escape" tag line
60 minute game. Team work. 2-6 players. All ages.
Should not have
• Cartoons, characters, people

```html
<!DOCTYPE html>
<html lang="en">
<head>
<meta charset="utf-8">
<title>The Lock Box – Escape Room Flyer</title>
<link href="https://fonts.googleapis.com/css2?family=Oswald:wght@400;500;600;700&family=Saira+Stencil+One&display=swap" rel="stylesheet">
<style>
  :root {
    --page: #e9e9ea;
    --ink: #050505;
    --orange: #f26522;
    --orange-line: #e0781f;
    --gold: #d9a441;
    --white: #ffffff;
    --grey: #d4d4d4;
  }
  * { box-sizing: border-box; margin: 0; padding: 0; }
  html, body { width: 1200px; height: 1200px; overflow: hidden; }
  body {
    background: var(--page);
    font-family: "Oswald", "Arial Narrow", sans-serif;
    position: relative;
  }
  .flyer {
    position: absolute;
    left: 50px; top: 211px;
    width: 1100px; height: 778px;
    background: var(--ink);
    overflow: hidden;
    box-shadow: 0 14px 40px rgba(0,0,0,.35);
  }
  .key-photo {
    position: absolute;
    left: 250px; top: 30px;
    width: 700px; height: 560px;
    background:
      radial-gradient(ellipse 30% 22% at 42% 52%, rgba(170,180,230,.55), transparent 70%),
      radial-gradient(ellipse 45% 40% at 62% 30%, rgba(95,70,55,.75), transparent 75%),
      radial-gradient(ellipse 50% 50% at 40% 55%, rgba(70,50,40,.8), transparent 80%);
  }
  .title-box {
    position: absolute;
    border: 1.5px solid var(--orange-line);
    border-radius: 34px;
    background: rgba(0,0,0,.55);
    text-transform: uppercase;
    text-align: center;
    line-height: .98;
    font-weight: 600;
    white-space: nowrap;
  }
  .title-box .line-white { color: var(--white); display: block; }
  .title-box .line-orange { color: var(--orange); display: block; }
  .title-box::after {
    content: "";
    position: absolute;
    left: 30%; right: 30%; bottom: -2px; height: 3px;
    background: linear-gradient(90deg, transparent, #ffd58a, transparent);
  }
  .room-coming {
    left: 600px; top: 50px; width: 420px; height: 180px;
    padding-top: 24px; font-size: 58px;
  }
  .room-coming .coming-soon {
    position: absolute; right: 28px; bottom: -20px;
    font-size: 24px; font-weight: 500; line-height: 1.3;
    color: var(--gold); background: var(--ink); padding: 0 8px;
  }
  .room-open {
    left: 110px; top: 215px; width: 430px; height: 185px;
    padding-top: 30px; font-size: 60px;
  }
  .brand {
    position: absolute; left: 60px; top: 520px;
    display: flex; align-items: center; gap: 14px;
    color: var(--gold); font-size: 38px; font-weight: 600;
    text-transform: uppercase; white-space: nowrap;
  }
  .brand .mark {
    width: 32px; height: 32px; border-radius: 50%;
    background: var(--gold);
  }
  .details {
    position: absolute; left: 360px; top: 425px; right: 30px;
    text-transform: uppercase; white-space: nowrap;
  }
  .tagline {
    font-size: 38px; font-weight: 700; line-height: 1.05;
    color: var(--white);
  }
  .tagline .few { color: var(--orange); }
  .facts {
    margin-top: 8px; font-size: 27px; font-weight: 500; line-height: 1.2;
    color: var(--white);
    padding-bottom: 10px; border-bottom: 1.5px solid var(--orange-line);
  }
  .facts .hl { color: var(--orange); }
  .contact {
    margin-top: 12px; display: flex; gap: 22px; align-items: center;
    font-size: 27px; font-weight: 500; line-height: 1.2; color: var(--white);
  }
  .contact span { display: inline-flex; align-items: center; gap: 8px; flex: none; }
  .contact .web { color: var(--grey); }
  .bookings {
    margin-top: 12px; margin-left: 60px;
    font-family: "Saira Stencil One", "Oswald", sans-serif;
    font-size: 42px; line-height: 1.1; color: var(--orange); letter-spacing: 6px;
  }
  .band {
    position: absolute; left: 0; right: 0; bottom: 0; height: 74px;
    background: var(--orange);
    display: flex; align-items: center; justify-content: center;
    font-size: 38px; font-weight: 600; text-transform: uppercase;
    color: var(--ink); letter-spacing: 1px; white-space: nowrap;
  }
</style>
</head>
<body>
  <main class="flyer">
    <div class="key-photo" role="img" aria-label="Photograph of an old iron key in a glowing keyhole on a dark wooden door"></div>

    <div class="title-box room-coming">
      <span class="line-white">Varuna's</span>
      <span class="line-orange">Vault</span>
      <span class="coming-soon">Coming soon</span>
    </div>

    <div class="title-box room-open">
      <span class="line-white">The Miller's</span>
      <span class="line-orange">Shadows</span>
    </div>

    <div class="brand"><span class="mark"></span>The Lock Box</div>

    <section class="details">
      <p class="tagline">Many will enter. . . <span class="few">Few will escape</span></p>
      <p class="facts"><span class="hl">60 minute game.</span> Team work. <span class="hl">2-6 players.</span> All ages.</p>
      <p class="contact">
        <span>
          <svg width="24" height="24" viewBox="0 0 24 24" aria-hidden="true"><path fill="#f26522" d="M6.6 10.8a15.1 15.1 0 0 0 6.6 6.6l2.2-2.2a1 1 0 0 1 1-.25 11.4 11.4 0 0 0 3.6.57 1 1 0 0 1 1 1V20a1 1 0 0 1-1 1A17 17 0 0 1 3 4a1 1 0 0 1 1-1h3.5a1 1 0 0 1 1 1c0 1.25.2 2.45.57 3.57a1 1 0 0 1-.25 1z"/></svg>
          0417 265 839.
        </span>
        <span class="web">
          <svg width="24" height="24" viewBox="0 0 24 24" aria-hidden="true" fill="none" stroke="#f26522" stroke-width="1.8"><circle cx="12" cy="12" r="9"/><ellipse cx="12" cy="12" rx="4" ry="9"/><path d="M3 12h18M5 7h14M5 17h14"/></svg>
          www.thelockboxhartwell.com
        </span>
      </p>
      <p class="bookings">Bookings essential</p>
    </section>

    <footer class="band">An unforgettable live-action gaming experience.</footer>
  </main>
</body>
</html>
```